Autobody repair paint repairs spray painting bodywork crash repairs

Details for my new Facebook Design Project will be added sooAUTOMOTIVE REPAIR. CAR / MOTORCYCLES GOT LOGO DESIGN / DID THINK ABOUT FACEBOOK DONT NOALREADY HAVE WEB ADRESS www.brightpanel.co.uk and mail sales@brightpanel,co.uk NEED SOMETHINK I CAN MANAGE TO UPLOAD PICTURES IN TO A GALLERY OR SOMETHINGLIKE THAT I ALSO SELL CAR AND MOTORCYCLES MAYBE A SELLS PAGE WITH A COINDROP LINKn.
Updates

Target Market(s)

general public and trade

Industry/Entity Type

Auto Repair

Font styles to use
Serif
Sans Serif

Colors

Designer to choose colors to be used in the design.

Requirements
Must have
• copy description from my website
• coindrop link. to my site shop
• plenty of logo within reason
Nice to have
• scolling shop
• easy to manage

```html
<!DOCTYPE html>
<html lang="en">
<head>
<meta charset="utf-8">
<title>Brightpanel Bodyshop – Cover</title>
<link rel="stylesheet" href="https://fonts.googleapis.com/css2?family=Montserrat:wght@400;500;600;700;800&display=swap">
<style>
  :root{
    --navy:#1c2129;
    --navy-deep:#14181e;
    --red:#e3262b;
    --red-dark:#c41d22;
    --white:#ffffff;
    --silver:#d9dce1;
    --ink:#15181d;
    --line:#5a606a;
  }
  *{margin:0;padding:0;box-sizing:border-box}
  html,body{width:1200px;height:457px;overflow:hidden;background:var(--white)}
  body{font-family:"Montserrat",Arial,sans-serif;color:var(--white)}
  .cover{position:relative;width:1200px;height:457px;overflow:hidden;background:#f3f3f4}

  .showcase-photo{position:absolute;left:400px;top:0;width:800px;height:400px;
    background:linear-gradient(100deg,#e9e2e2 0%,#d9c9c9 35%,#c9c3c3 60%,#e7e7e7 100%)}
  .shapes{position:absolute;inset:0}

  .brand{position:absolute;left:36px;top:78px;width:350px;text-align:center}
  .brand-name{font-weight:800;font-size:35px;letter-spacing:1px;color:var(--silver);line-height:1}
  .brand-sub{margin-top:12px;font-weight:500;font-size:14px;letter-spacing:7px;color:var(--white)}

  .tagline-pill{position:absolute;left:132px;top:186px;width:188px;height:33px;border-radius:9px;
    background:var(--red);font-weight:700;font-size:15px;text-align:center;line-height:33px}
  .tagline-main{position:absolute;left:36px;top:226px;width:350px;text-align:center;
    font-weight:800;font-size:22px;letter-spacing:.5px}
  .divider{position:absolute;left:36px;top:281px;width:350px;height:1px;background:var(--line)}

  .contact{position:absolute;display:flex;align-items:center}
  .contact-phone{left:48px;top:306px;gap:14px}
  .contact-phone span{font-size:33px;font-weight:400;letter-spacing:.5px}
  .contact-address{left:50px;top:380px;gap:20px}
  .contact-address span{font-size:15.5px;font-weight:500;line-height:1.45}

  .services-tab{position:absolute;left:446px;top:30px;width:192px;height:34px;background:var(--navy);
    font-weight:600;font-size:19px;line-height:34px;padding-left:16px;letter-spacing:.5px}
  .services{position:absolute;left:490px;top:74px;display:grid;grid-template-columns:298px 360px;
    column-gap:0;row-gap:3px;list-style:none;color:var(--ink);font-weight:600;font-size:18.5px;line-height:1.2}
  .services li{display:flex;align-items:flex-start;gap:8px}
  .services svg{flex:none;margin-top:3px}

  .footer-links{position:absolute;left:586px;top:405px;display:flex;align-items:center;gap:10px;
    font-size:20px;font-weight:500}
</style>
</head>
<body>
<main class="cover">
  <div class="showcase-photo" role="img" aria-label="Photo of a row of cars in for bodywork – a yellow hatchback, a black classic coupe, a red sports car, an engine block and a bright green hatchback in a spray booth"></div>

  <svg class="shapes" width="1200" height="457" viewBox="0 0 1200 457" aria-hidden="true">
    <polygon points="0,0 444,0 556,457 0,457" fill="var(--navy)"/>
    <polygon points="400,0 444,0 458,57 " fill="var(--red)"/>
    <polygon points="444,0 456,0 568,457 556,457" fill="var(--red)"/>
    <polygon points="556,393 1200,393 1200,457 572,457" fill="var(--red)"/>
    <path d="M638 62 H1165 Q1176 62 1176 73 V100" fill="none" stroke="var(--navy)" stroke-width="2"/>
  </svg>

  <div class="brand">
    <div class="brand-name">BRIGHTPANEL</div>
    <div class="brand-sub">BODYSHOP</div>
  </div>

  <div class="tagline-pill">WE ARE YOUR ONE</div>
  <div class="tagline-main">STOP BODYSHOP</div>
  <div class="divider"></div>

  <div class="contact contact-phone">
    <svg width="30" height="32" viewBox="0 0 24 24" fill="none" stroke="#fff" stroke-width="1.8" stroke-linecap="round">
      <path d="M5 3h3l2 5-2 1.5a11 11 0 0 0 6 6L15.5 13l5 2v3a2 2 0 0 1-2 2A16 16 0 0 1 3 5a2 2 0 0 1 2-2z"/>
      <path d="M14 3a7 7 0 0 1 7 7M14 6.5a3.5 3.5 0 0 1 3.5 3.5"/>
    </svg>
    <span>07700900461</span>
  </div>

  <div class="contact contact-address">
    <svg width="26" height="34" viewBox="0 0 24 30" fill="none" stroke="#fff" stroke-width="2">
      <path d="M12 28s9-9.5 9-16a9 9 0 0 0-18 0c0 6.5 9 16 9 16z"/>
      <circle cx="12" cy="12" r="3.5"/>
    </svg>
    <span>Kestrel Business park, Ash Lane, Holbrook,<br>Derbyshire, DE56 0XQ</span>
  </div>

  <div class="services-tab">WHAT WE DO</div>
  <ul class="services">
    <li><svg width="16" height="16" viewBox="0 0 16 16"><circle cx="8" cy="8" r="8" fill="var(--red)"/><path d="M4.5 8.2l2.3 2.3 4.7-4.8" fill="none" stroke="#fff" stroke-width="1.8"/></svg>Full or part resprays</li>
    <li><svg width="16" height="16" viewBox="0 0 16 16"><circle cx="8" cy="8" r="8" fill="var(--red)"/><path d="M4.5 8.2l2.3 2.3 4.7-4.8" fill="none" stroke="#fff" stroke-width="1.8"/></svg>Accident repair</li>
    <li><svg width="16" height="16" viewBox="0 0 16 16"><circle cx="8" cy="8" r="8" fill="var(--red)"/><path d="M4.5 8.2l2.3 2.3 4.7-4.8" fill="none" stroke="#fff" stroke-width="1.8"/></svg>Dents &amp; scratch removal</li>
    <li><svg width="16" height="16" viewBox="0 0 16 16"><circle cx="8" cy="8" r="8" fill="var(--red)"/><path d="M4.5 8.2l2.3 2.3 4.7-4.8" fill="none" stroke="#fff" stroke-width="1.8"/></svg><span>Alloy wheel’s refurbished,<br>Repaired &amp; Painted</span></li>
    <li style="margin-top:-24px"><svg width="16" height="16" viewBox="0 0 16 16"><circle cx="8" cy="8" r="8" fill="var(--red)"/><path d="M4.5 8.2l2.3 2.3 4.7-4.8" fill="none" stroke="#fff" stroke-width="1.8"/></svg>Bumper repair</li>
  </ul>

  <div class="footer-links">
    <svg width="26" height="24" viewBox="0 0 26 24" fill="none" stroke="#fff" stroke-width="1.8" stroke-linejoin="round">
      <path d="M2 10l11-8 11 8v12H2z"/><path d="M2 10l11 7 11-7"/><path d="M6 7h14"/>
    </svg>
    <span>sales@brightpanel.co.uk | www.brightpanel.co.uk</span>
    <svg width="26" height="26" viewBox="0 0 24 24" fill="none" stroke="#fff" stroke-width="1.6" style="margin-left:12px">
      <circle cx="12" cy="12" r="10"/><ellipse cx="12" cy="12" rx="4.5" ry="10"/><path d="M2 12h20M4 6.5h16M4 17.5h16"/>
    </svg>
  </div>
</main>
</body>
</html>
```